Premium Wraparound Label Design for 6 oz Guava Butter Jar – Lanikeo Sweet Kitchen

Design a continuous wraparound label for an 6 oz circular glass jar that integrates the Lanikeo Sweet Kitchen logo (featuring the pink and brown leaf motif) and the Guava Butter nutrition label into one cohesive, premium presentation. The design should feel authentically Hawaiian, classic, and handcrafted—reflecting the brand’s legacy of island-inspired desserts.
Label Specifications
Container: 8 oz round glass jar
Label Type: Full wraparound (one continuous label)
Approximate Label Size: 2.5 inches tall × 8.5 inches wide
Finish: Matte or satin with optional gold foil highlights
Print: CMYK-ready artwork with bleed and safe zones clearly marked
Design Elements to Integrate
1. Front Panel (Main Display Area):
Prominently feature the Lanikeo Sweet Kitchen logo centered and scaled proportionally.
Display the product name “Guava Butter” in elegant, legible typography that complements the logo.
Add the following text beneath or near the product name:
“Made in Hawai‘i”
“Net Wt. 8 oz (227g)”
“Keep Refrigerated” (in smaller but clear type).
Background tones should complement the logo—cream, soft tan, or pastel pink for warmth and harmony.
The front should communicate island sophistication—premium yet inviting.
2. Side Panel (Transition Area):
Create a smooth visual transition around the jar using a subtle, continuous background pattern such as tropical leaves, ocean wave textures, or gold accent lines.
Include the brand story text:
“Lanikeo Sweet Kitchen brings authentic island flavors to every table. Our signature Guava Butter blends tropical fruit and fresh cream for a taste of pure aloha.”
3. Back Panel (Informational Area):
Integrate the Guava Butter nutrition facts panel and ingredients list (from the attached file).
Ensure layout is FDA-compliant, legible, and well-balanced.
Beneath the ingredients, include:
“Manufactured by Lanikeo Sweet Kitchen, Hawai‘i.”
“Keep Refrigerated.”
Leave space for:
A QR code linking to the brand website and social media.
A barcode area, placed neatly near the bottom or corner.
Aesthetic Direction
Style: Premium, classic, and island-inspired
Color Palette: Cream base with warm browns, muted pinks, and gold accents
Typography:
Serif or script for product name and logo (for a classic, handcrafted look)
Clean sans-serif for informational text
Mood: Heritage meets handcrafted luxury — nostalgic yet refined
Finish Options:
Matte for artisanal authenticity
Satin or metallic foil for a modern, premium touch
Deliverables
Designers should submit:
3 design variations (e.g., classic heritage, minimalist modern, and premium tropical).
Editable source files (AI, PSD, or layered PDF) with bleed and safe zones clearly marked.
Mockups on an 8 oz round glass jar for visual presentation.

Target Market(s)

Craft fair consumers / tourist in hawaii

Industry/Entity Type

food and Bev

Logo Text

see description

Font styles to use
Serif
Sans Serif
Script

Requirements
Must have
• see description
Nice to have
• see description
Should not have
• see description

```html
<!DOCTYPE html>
<html lang="en">
<head>
<meta charset="utf-8">
<title>Lanikeo Sweet Kitchen – Guava Butter Wraparound Label</title>
<link rel="stylesheet" href="https://fonts.googleapis.com/css2?family=Cinzel:wght@500&family=Montserrat:wght@500;600&family=Cormorant+Garamond:wght@600&family=Arimo:wght@400;700;800&display=swap">
<style>
  :root {
    --page: #ffffff;
    --blush: #f7dedb;
    --blush-light: #fae8e5;
    --blush-deep: #efcdc9;
    --rose: #c0767a;
    --rose-soft: #e7b9b7;
    --cocoa: #4a2a1a;
    --ink: #111111;
    --panel: #fbeeee;
  }
  * { margin: 0; padding: 0; box-sizing: border-box; }
  html, body { width: 1200px; height: 1200px; overflow: hidden; background: var(--page); }
  .canvas { position: relative; width: 1200px; height: 1200px; }

  .label {
    position: absolute; left: 128px; top: 420px; width: 750px; height: 221px;
    background: var(--blush); overflow: hidden;
  }
  .leaf-texture {
    position: absolute; inset: 0;
    background: radial-gradient(ellipse at 30% 70%, var(--blush-deep), transparent 55%),
                radial-gradient(ellipse at 70% 30%, var(--blush-light), transparent 60%);
  }

  /* story side */
  .story-frame {
    position: absolute; left: 9px; top: 8px; width: 116px; height: 204px;
    border: 1.5px solid var(--rose);
    padding: 20px 8px 0;
    font-family: "Montserrat", sans-serif; font-weight: 500; font-size: 9.6px; line-height: 1.3;
    color: var(--rose); text-align: center;
  }
  .story-frame p + p { margin-top: 12px; }
  .story-frame strong { font-weight: 600; }
  .story-rule { position: absolute; left: 28px; right: 28px; bottom: 16px; border-top: 1.5px solid var(--rose); }

  /* front */
  .origin-badge { position: absolute; left: 166px; top: 0; width: 52px; height: 78px; }
  .origin-badge svg { position: absolute; inset: 0; }
  .origin-badge span {
    position: absolute; left: 0; right: 0; top: 41px;
    font-family: "Montserrat", sans-serif; font-weight: 600; font-size: 8px; line-height: 1.2;
    color: #ffffff; text-align: center;
  }
  .brand-dot { position: absolute; left: 345px; top: 38px; width: 44px; height: 44px; border-radius: 50%; background: var(--rose-soft); }
  .brand-name {
    position: absolute; left: 200px; width: 335px; top: 100px; text-align: center;
    font-family: "Cinzel", serif; font-weight: 500; color: var(--cocoa);
  }
  .brand-name .line-1 { display: block; font-size: 38px; letter-spacing: 1px; line-height: 40px; }
  .brand-name .line-2 { display: block; font-size: 19px; letter-spacing: 1.5px; line-height: 24px; }
  .established {
    position: absolute; left: 322px; width: 92px; top: 178px;
    display: flex; align-items: center; gap: 5px;
    font-family: "Montserrat", sans-serif; font-size: 8px; letter-spacing: 1px; color: var(--cocoa);
  }
  .established::before, .established::after { content: ""; flex: 1; border-top: 1px solid var(--cocoa); }
  .product-ribbon { position: absolute; left: 302px; top: 196px; width: 132px; height: 17px; }
  .product-ribbon svg { position: absolute; inset: 0; }
  .product-ribbon span {
    position: absolute; inset: 0; text-align: center; line-height: 17px;
    font-family: "Cormorant Garamond", serif; font-weight: 600; font-size: 14px; letter-spacing: 1px; color: #ffffff;
  }
  .net-weight {
    position: absolute; right: 218px; top: 190px; text-align: right;
    font-family: "Montserrat", sans-serif; font-size: 7.5px; line-height: 1.3; color: var(--cocoa);
  }

  /* nutrition */
  .nutrition {
    position: absolute; left: 616px; top: 0; width: 104px; height: 221px; background: var(--panel);
    padding: 3px 4px; font-family: "Arimo", sans-serif; color: var(--ink); font-size: 4.2px; line-height: 1.4;
    border-left: 1px solid var(--ink);
  }
  .nutrition h2 { font-weight: 800; font-size: 12.5px; line-height: 14px; white-space: nowrap; border-bottom: 1px solid var(--ink); }
  .nutrition .bar-thick { border-top: 3px solid var(--ink); }
  .nutrition .bar-mid { border-top: 1.5px solid var(--ink); }
  .nutrition .row { border-top: 0.5px solid var(--ink); display: flex; justify-content: space-between; }
  .nutrition .indent { padding-left: 6px; }
  .nutrition .calories { display: flex; justify-content: space-between; font-weight: 800; font-size: 9px; line-height: 11px; }
  .nutrition b { font-weight: 700; }
  .nutrition .dv { text-align: right; font-weight: 700; border-top: 1px solid var(--ink); }
  .nutrition .ingredients { margin-top: 2px; line-height: 1.45; }

  .maker-strip { position: absolute; left: 720px; top: 0; width: 30px; height: 221px; background: var(--rose); }
  .maker-text {
    position: absolute; left: 15px; top: 110px; width: 205px; transform: translate(-50%, -50%) rotate(-90deg);
    font-family: "Montserrat", sans-serif; font-size: 7px; line-height: 1.35; color: var(--rose-soft);
  }
  .maker-text strong { font-weight: 600; }
</style>
</head>
<body>
<main class="canvas">
  <section class="label">
    <div class="leaf-texture" role="img" aria-label="Faint tropical leaf pattern across the label background"></div>

    <aside class="story-frame">
      <p><strong>Lanikeo Sweet Kitchen</strong> brings authentic island flavors to every table.</p>
      <p>Our signature <strong>Guava Butter</strong> blends tropical fruit and fresh cream for a taste of pure aloha.</p>
      <div class="story-rule"></div>
    </aside>

    <div class="origin-badge">
      <svg width="52" height="78" viewBox="0 0 52 78">
        <rect x="15" y="0" width="22" height="28" fill="var(--rose)"/>
        <circle cx="26" cy="50" r="23" fill="var(--rose)"/>
        <circle cx="26" cy="50" r="24" fill="none" stroke="var(--rose)" stroke-width="5" stroke-linecap="round" stroke-dasharray="0 9.4"/>
      </svg>
      <span>MADE IN<br>HAWAI'I</span>
    </div>

    <div class="brand-dot"></div>
    <h1 class="brand-name">
      <span class="line-1">LANIKEO</span>
      <span class="line-2">SWEET KITCHEN</span>
    </h1>
    <div class="established">EST.1999</div>
    <div class="product-ribbon">
      <svg width="132" height="17" viewBox="0 0 132 17">
        <path d="M0 0 H132 L126 8.5 L132 17 H0 L6 8.5 Z" fill="var(--rose)"/>
      </svg>
      <span>GUAVA BUTTER</span>
    </div>
    <p class="net-weight">NET WT.<br>8 OZ (227G)</p>

    <section class="nutrition">
      <h2>Nutrition Facts</h2>
      <div>Serving Size 1 serving</div>
      <div class="bar-thick"><b>Amount Per Serving</b></div>
      <div class="calories"><span>Calories</span><span>150</span></div>
      <div class="dv">% Daily Value*</div>
      <div class="row"><span><b>Total Fat</b> 13g</span></div>
      <div class="row indent"><span>Saturated Fat 8g</span></div>
      <div class="row indent"><span>Trans Fat 0g</span></div>
      <div class="row"><span><b>Cholesterol</b> 55mg</span></div>
      <div class="row"><span><b>Sodium</b> 5mg</span></div>
      <div class="row"><span><b>Total Carbohydrate</b> 10g</span></div>
      <div class="row indent"><span>Dietary Fiber 0g</span></div>
      <div class="row indent"><span>Total Sugars 8g</span></div>
      <div class="row indent"><span>Includes Added Sugars 8g</span></div>
      <div class="row"><span><b>Protein</b> 1g</span></div>
      <div class="bar-thick"></div>
      <div class="row"><span>Vitamin D 10% DV</span><span>Calcium 2% DV</span></div>
      <div class="row"><span>Iron 0% DV</span><span>Potassium 1% DV</span></div>
      <div class="bar-mid ingredients"><b>Ingredients:</b> Guava concentrate, Unsalted butter (cream, natural flavor), Cane sugar, Whole eggs, Egg yolks, Proprietary blend of natural flavors and spices.</div>
    </section>

    <div class="maker-strip">
      <p class="maker-text">Manufactured by <strong>Lanikeo Sweet Kitchen</strong>, Hawai'i.<br>Keep Refrigerated.</p>
    </div>
  </section>
</main>
</body>
</html>
```